Employees at T&M Gale Power Solutions need new modern business cards

We need new business cards that showcase our new rebranded logo. We are seeking modern, clean, fresh, attractive cards while still being professional. We want to stand out. A little bit about us: we work in Canada and the USA. We offer Technical Field Advisors to support wind turbine manufacturers through the construction phase of wind farms. I am attaching a mock inspiration picture to lead you in the direction we want to see this go. Also, FYI We have approx. 10/11 different employees that would need their own card. Let me know when you would need everyone's name. We would love to see some black and white options as well as color copies- when using colors we want green to be the dominant color with accents for blue and orange (colors should match our logo). I have also attached copies of our old business card for reference.

Contact Information for Business Card

Name, Telephone, Email, address, company name, website. EXAMPLE: Hugh Marlow, HughMarlow@tandmgale.example, 555-381-4926, 217763 Birch Line #9, Elmhurst, ON X1Y 2Z3, www.tandmgale.example

Colors
0054AA
0677BA
7BADD7
CADEEF
E8F1F8
00AB8E
00BBA5
67D7C9
C6EFE9
E9F9F6
F0912C
F2A743
F7CA91
FBE8D2
FDF5EE

Requirements
Must have
• 2 sided business card

```html
<!DOCTYPE html>
<html lang="en">
<head>
<meta charset="utf-8">
<title>T&amp;M Gale Power Solutions – Business Card</title>
<link rel="stylesheet" href="https://fonts.googleapis.com/css2?family=Roboto:wght@400;500&display=swap">
<style>
  :root {
    --page-bg: #ece7de;
    --card-white: #ffffff;
    --card-black: #202020;
    --brand-green: #2eb047;
    --brand-blue: #1677c4;
    --brand-orange: #f39c1f;
    --text-dark: #333333;
    --emboss-grey: #b9b9b9;
  }
  * { margin: 0; padding: 0; box-sizing: border-box; }
  html, body {
    width: 1200px; height: 1200px; overflow: hidden;
    background: var(--page-bg);
    font-family: "Roboto", Arial, sans-serif;
  }
  .card {
    position: absolute;
    left: 281px;
    width: 640px; height: 366px;
    border-radius: 18px;
  }
  .card-front { top: 195px; background: var(--card-white); }
  .card-back { top: 639px; background: var(--card-black); }

  /* front: brand block */
  .brand-mark {
    position: absolute; left: 470px; top: 34px;
    width: 86px; height: 86px; border-radius: 50%;
    border: 5px solid var(--brand-green);
  }
  .brand-name {
    position: absolute; right: 32px; top: 132px;
    text-align: right;
    font-size: 21px; font-weight: 500; line-height: 1.2;
    letter-spacing: 1.5px; text-transform: uppercase;
    color: var(--brand-green);
  }

  /* front: person */
  .person-name {
    position: absolute; left: 33px; top: 206px;
    font-size: 24px; font-weight: 500; letter-spacing: -0.3px;
    color: var(--brand-blue); text-transform: uppercase;
  }
  .person-title {
    position: absolute; left: 33px; top: 234px;
    font-size: 16px; font-weight: 400;
    color: var(--brand-green);
  }

  .divider {
    position: absolute; top: 264px; height: 3px; width: 188px;
  }
  .divider-blue { left: 33px; background: var(--brand-blue); }
  .divider-green { left: 226px; background: var(--brand-green); }
  .divider-orange { left: 420px; background: var(--brand-orange); }

  .contact-list {
    position: absolute; left: 33px; top: 280px;
    list-style: none;
    font-size: 15px; line-height: 18px; color: var(--text-dark);
  }
  .contact-list li { display: flex; align-items: center; height: 18px; }
  .contact-icon { width: 12px; height: 12px; margin-right: 8px; flex: none; }

  .address {
    position: absolute; right: 32px; top: 280px;
    text-align: right; font-style: normal;
    font-size: 15px; line-height: 18px; color: var(--text-dark);
  }

  /* back */
  .back-mark {
    position: absolute; left: 249px; top: 76px;
    width: 140px; height: 140px; border-radius: 50%;
    border: 6px solid var(--emboss-grey);
  }
  .back-name {
    position: absolute; left: 0; right: 0; top: 236px;
    text-align: center;
    font-size: 28px; font-weight: 500; line-height: 1.2;
    letter-spacing: 3px; text-transform: uppercase;
    color: var(--emboss-grey);
  }
</style>
</head>
<body>

<section class="card card-front" aria-label="Business card front">
  <div class="brand-mark" aria-hidden="true"></div>
  <div class="brand-name">T&amp;M Gale<br>Power Solutions</div>

  <h1 class="person-name">Hugh Marlow</h1>
  <p class="person-title">Owner &amp; CEO</p>

  <div class="divider divider-blue"></div>
  <div class="divider divider-green"></div>
  <div class="divider divider-orange"></div>

  <ul class="contact-list">
    <li>
      <svg class="contact-icon" viewBox="0 0 12 12" aria-hidden="true">
        <path d="M2.5 1 L4.5 1 L5 3.5 L3.8 4.5 C4.5 6 6 7.5 7.5 8.2 L8.5 7 L11 7.5 L11 9.5 C11 10.3 10.3 11 9.5 11 C5 10.6 1.4 7 1 2.5 C1 1.7 1.7 1 2.5 1 Z" fill="var(--brand-orange)"/>
      </svg>
      555-381-4926
    </li>
    <li>
      <svg class="contact-icon" viewBox="0 0 12 12" aria-hidden="true">
        <rect x="0.5" y="2.5" width="11" height="7.5" fill="var(--brand-orange)"/>
        <path d="M0.8 2.8 L6 6.8 L11.2 2.8" fill="none" stroke="#fff" stroke-width="1"/>
      </svg>
      HughMarlow@tandmgale.example
    </li>
    <li>
      <svg class="contact-icon" viewBox="0 0 12 12" aria-hidden="true">
        <circle cx="6" cy="6" r="5.5" fill="var(--brand-orange)"/>
        <path d="M6 0.5 C3.5 3 3.5 9 6 11.5 M6 0.5 C8.5 3 8.5 9 6 11.5 M0.5 6 H11.5" fill="none" stroke="#fff" stroke-width="0.8"/>
      </svg>
      www.tandmgale.example
    </li>
  </ul>

  <address class="address">
    T&amp;M Gale Power Solutions<br>
    217763 Birch Line #9<br>
    Elmhurst, ON X1Y 2Z3
  </address>
</section>

<section class="card card-back" aria-label="Business card back">
  <div class="back-mark" aria-hidden="true"></div>
  <div class="back-name">T&amp;M Gale<br>Power Solutions</div>
</section>

</body>
</html>
```